I work in creative/artistic projects across different mediums.
It needs to communicate creativity, style, sexy, uniqueness, individuality and sophistication.
It should not look corporate.
Colours I like are black silver gold deep purple, chocolate, orchid.
It doesn't have to make use of all these colours.
I do not like bright primary colors.
Updates

Project Deadline Extended
Reason: Still in the communication process and to allow the person enough time to finish the design. Though i should know in the next day or two. Thank you.

Target Market(s)

creatives and companies wanting to inject creativity into thier business.

Industry/Entity Type

Work

Contact Information for Business Card

Marcus Tellwick
0418592036
marcus@marcustellwick.com

quietgoldenhour.com.au

Requirements
Should not have
• Anything corporate OR OLD FASHIONED

```html
<!DOCTYPE html>
<html lang="en">
<head>
<meta charset="utf-8">
<title>Marcus Tellwick — Business Card</title>
<link rel="stylesheet" href="https://fonts.googleapis.com/css2?family=Pinyon+Script&family=Didact+Gothic&display=swap">
<style>
  :root {
    --backdrop: #e9e5df;
    --card-black: #0b0b0c;
    --card-edge: #1a1a1c;
    --damask-tone: #1c1c1f;
    --gold-light: #f3dc9a;
    --gold-mid: #d4a544;
    --gold-deep: #9c6a1e;
    --orchid: #b24fd6;
  }
  * { margin: 0; padding: 0; box-sizing: border-box; }
  html, body {
    width: 1200px;
    height: 1023px;
    overflow: hidden;
    background: var(--backdrop);
  }
  .canvas {
    position: relative;
    width: 1200px;
    height: 1023px;
  }
  .business-card {
    position: absolute;
    left: 150px;
    top: 254px;
    width: 900px;
    height: 514px;
    border-radius: 34px;
    background: var(--card-black);
    overflow: hidden;
    box-shadow: 0 18px 40px rgba(0,0,0,0.25);
  }
  .damask-field {
    position: absolute;
    inset: 0;
    background:
      radial-gradient(ellipse at 30% 40%, var(--damask-tone) 0%, transparent 55%),
      radial-gradient(ellipse at 75% 65%, var(--damask-tone) 0%, transparent 50%),
      linear-gradient(135deg, var(--card-black), var(--card-edge) 50%, var(--card-black));
  }
  .website {
    position: absolute;
    left: 44px;
    top: 40px;
    font-family: "Didact Gothic", sans-serif;
    font-size: 19px;
    letter-spacing: 0.5px;
    color: var(--orchid);
  }
  .holder-name {
    position: absolute;
    left: 0;
    right: 0;
    top: 170px;
    text-align: center;
    font-family: "Pinyon Script", cursive;
    font-size: 96px;
    line-height: 1.2;
    background: linear-gradient(180deg, var(--gold-light) 0%, var(--gold-mid) 55%, var(--gold-deep) 100%);
    -webkit-background-clip: text;
    background-clip: text;
    color: transparent;
  }
  .contact-details {
    position: absolute;
    right: 60px;
    bottom: 44px;
    text-align: left;
    font-family: "Didact Gothic", sans-serif;
    font-size: 26px;
    line-height: 1.65;
    letter-spacing: 0.6px;
    color: var(--orchid);
  }
</style>
</head>
<body>
<main class="canvas">
  <section class="business-card">
    <div class="damask-field" role="img" aria-label="Subtle dark damask floral pattern across the black card"></div>
    <p class="website">www.quietgoldenhour.com.au</p>
    <h1 class="holder-name">Marcus Tellwick</h1>
    <div class="contact-details">
      <p class="phone">0418592036</p>
      <p class="email">marcus@marcustellwick.com</p>
    </div>
  </section>
</main>
</body>
</html>
```